Web Design Project

This web site is to be designed for a popular Cambodian singer, Pich Leakena. Web site name "Pich Leakena".

The purpose is to keep her fans update with the latest of her entertainment career and invite them to help raising fund for Mekong Little Hands Fund.

In addition to other normal pages such as HOME, ABOUT... This web site must be:
1. able to link to Dropshipers and add Products
2. able to donate (accept Major Credit Cards or CoinLark)
3. able to purchase products (accept Major Credit Cards or CoinLark)
4. able to video live chat with Pich Leakena
5. able to book appointment on her calendar

Here is a sample of the web site:
http://dorvel22.sitebarn.example/pich-lea-kena

Please call me if you need any clarification at 1-555-284-1937 or leave your number for me to call you back.

Thank you

Vuthy

Target Market(s)

Cambodian living abroad

Industry/Entity Type

Entertainment

Requirements
Must have
• 1. able to link to Dropshipers and add Products
2. able to Donate (accept Major Credit Cards or CoinLark)

```html
<!DOCTYPE html>
<html lang="en">
<head>
<meta charset="utf-8">
<title>Pich Leakena</title>
<link href="https://fonts.googleapis.com/css2?family=Arimo:wght@400;700&family=Noto+Serif:wght@400;700&display=swap" rel="stylesheet">
<style>
:root{
  --page-bg:#0b0b0b;
  --panel-dark:#1e1e1e;
  --nav-dark:#262626;
  --brand-red:#e10600;
  --button-red:#c8000a;
  --button-dark:#333;
  --text-dark:#111;
  --text-muted:#8a8a8a;
  --line:#dcdcdc;
  --white:#fff;
}
*{box-sizing:border-box;margin:0;padding:0}
html,body{width:1136px;height:1200px;overflow:hidden}
body{background:var(--page-bg);font-family:Arimo,Arial,sans-serif;color:var(--text-dark);position:relative}
.page{position:absolute;left:168px;top:0;width:800px;height:1200px}
.site-header{position:relative;height:96px}
.brand{position:absolute;left:4px;top:30px;display:flex;align-items:center;gap:8px;font-family:"Noto Serif",serif;font-weight:700;font-size:25px;color:var(--brand-red);letter-spacing:1px}
.brand-mark{width:14px;height:14px;background:var(--brand-red)}
.top-links{position:absolute;right:8px;top:24px;display:flex;gap:17px;font-size:11.5px;color:var(--white)}
.account-bar{position:absolute;right:8px;top:50px;display:flex;align-items:center;gap:8px;font-size:9.5px;color:#bbb}
.account-bar .sep{color:#555}
.account-bar .muted{color:#777}
.account-bar .cart{color:var(--brand-red)}
.currency{background:#555;color:#ddd;padding:3px 5px;font-size:9.5px}
.main-nav{height:53px;background:linear-gradient(#2e2e2e,#1f1f1f);display:flex;align-items:center;position:relative}
.main-nav a{font-family:"Noto Serif",serif;font-size:15px;color:var(--white);text-decoration:none;padding:0 19px;border-right:1px solid #3c3c3c;line-height:28px}
.main-nav a:first-child{padding-left:25px}
.search{position:absolute;right:13px;top:13px;width:168px;height:26px;background:var(--white);border:1px solid #999;font-size:10px;color:#777;padding:7px 11px;display:flex;justify-content:space-between}
.hero{position:relative;height:301px;background:radial-gradient(circle at 30% 40%,#3c6e45,#143020 70%);overflow:hidden}
.hero-photo{position:absolute;right:0;top:0;width:340px;height:301px;background:linear-gradient(160deg,#6b8f3c,#c5cc55 60%,#d9d86a)}
.hero-copy{position:absolute;left:49px;top:88px;width:360px;color:var(--white);font-size:14px;line-height:24px}
.hero-copy p+p{margin-top:24px}
.dots{position:absolute;left:53px;top:270px;display:flex;gap:3px}
.dots span{width:14px;height:14px;border-radius:50%;background:#444}
.dots span.on{background:var(--brand-red)}
.content{position:absolute;top:450px;left:0;width:800px;height:709px;background:var(--white)}
.video{position:absolute;left:14px;top:13px;width:343px;height:195px;background:#000}
.video-frame{position:absolute;left:0;top:0;width:343px;height:176px;background:radial-gradient(circle at 30% 50%,#b8962c,#2a1c0c 55%,#050505)}
.play{position:absolute;left:151px;top:74px;width:40px;height:30px;background:#222;border:1px solid #555;border-radius:6px}
.play::after{content:"";position:absolute;left:15px;top:8px;border-left:12px solid var(--white);border-top:7px solid transparent;border-bottom:7px solid transparent}
.controls{position:absolute;left:0;bottom:0;width:343px;height:19px;background:#1a1a1a;font-size:6px;color:#aaa;padding:6px 0 0 53px}
.controls::before{content:"";position:absolute;left:0;top:0;width:80px;height:3px;background:var(--brand-red)}
.bio{position:absolute;left:366px;top:14px;width:422px;font-size:9.6px;line-height:16px;text-align:justify}
.bio p+p{margin-top:16px}
.bio a{color:var(--brand-red);text-decoration:none}
.section-title{position:absolute;left:21px;top:244px;font-family:"Noto Serif",serif;font-weight:400;font-size:12px;line-height:16px}
.rule{position:absolute;left:14px;width:770px;height:1px;background:var(--line)}
.product{position:absolute;top:286px;width:170px}
.product-image{width:130px;height:128px;margin-left:-2px}
.product-name{margin-top:12px;font-size:9.6px;line-height:14px;color:var(--text-muted)}
.price{margin-top:5px;font-size:12px;font-weight:700}
.actions{margin-top:10px;display:flex;gap:4px}
.btn{font-size:10px;font-weight:700;color:var(--white);padding:6px 6px;line-height:11px}
.btn-cart{background:var(--button-red)}
.btn-view{background:var(--button-dark)}
.feature{position:absolute;top:564px;width:246px;height:104px;background:var(--panel-dark);color:var(--white);padding:12px 15px}
.feature.red{background:var(--brand-red)}
.feature h3{font-family:"Noto Serif",serif;font-weight:400;font-size:12.5px;white-space:nowrap}
.feature p{font-size:9.6px;line-height:16px;width:140px;margin-top:3px}
.feature .cta{font-size:9.6px;margin-top:8px;display:block}
.feature-art{position:absolute;right:5px;top:34px;width:74px;height:98px}
.site-footer{position:absolute;top:1159px;left:0;width:800px;height:41px;background:var(--panel-dark);color:var(--white);font-size:9.6px;padding:8px 16px;line-height:14px}
.payments{position:absolute;right:16px;top:14px;display:flex;gap:4px;font-size:7px;color:#333}
.payments span{background:#eee;padding:3px 3px}
.payments .social{background:#3a6fb5;color:var(--white)}
</style>
</head>
<body>
<div class="page">
  <header class="site-header">
    <div class="brand"><span class="brand-mark"></span>PICH LEAKENA</div>
    <nav class="top-links"><span>HOME</span><span>SPECIALS</span><span>DELIVERY</span><span>CONTACTS</span></nav>
    <div class="account-bar">
      <span>Welcome</span><span class="sep">|</span><span class="muted">Your Account</span><span class="sep">|</span>
      <span><span class="cart">Cart:</span> (empty)</span><span class="sep">|</span>
      <span>Currencies:</span><span class="currency">US Dollar ▾</span>
    </div>
  </header>
  <nav class="main-nav">
    <a>HOME</a><a>ABOUT</a><a>PRODUCTS</a><a>FEEDBACK</a><a>DONATE</a>
    <div class="search"><span>Search</span>
      <svg width="10" height="10" viewBox="0 0 10 10"><circle cx="4" cy="4" r="3" fill="none" stroke="#333" stroke-width="1.4"/><line x1="6.2" y1="6.2" x2="9.5" y2="9.5" stroke="#333" stroke-width="1.6"/></svg>
    </div>
  </nav>
  <section class="hero">
    <div class="hero-photo" role="img" aria-label="Portrait photo of the singer in a green dress outdoors"></div>
    <div class="hero-copy">
      <p>&nbsp;I would like to keep you all update with the latest of my entertainment career</p>
      <p>Another purpose of this site is to help raising fund for Mekong Little Hands Fund</p>
    </div>
    <div class="dots"><span class="on"></span><span></span><span></span></div>
  </section>
  <main class="content">
    <div class="video">
      <div class="video-frame" role="img" aria-label="Video still of the singer performing on stage in a yellow dress"></div>
      <div class="play"></div>
      <div class="controls">0:02 / 0:10</div>
    </div>
    <div class="bio">
      <p>Since she was award as a top Female Cambodian signer in 1997, Leakena's atmospheric folk-pop, KunTrim has gained a devoted following of fans not only in Cambodia, where she has established popular star status but also in the U.S., Canada, Australia, France, New Zealand and around the world.</p>
      <p>Each album has shown her growing both as a musician and actress, continually redefining herself and emerging as a major voice in the growing alternative pop and Kun Trim format.</p>
      <p>Leakena was born in Battombang, Cambodia, on February 1st, 1978 where she went as an ordinary little girl helping parents to make a family living by selling fruits, Vegetable and Nom Kroch door to door. Leakena loves whisper singing while selling door to door.<br><a>Read more</a></p>
    </div>
    <h2 class="section-title">PRODUCTS</h2>
    <div class="rule" style="top:267px"></div>
    <div class="product" style="left:36px">
      <div class="product-image" role="img" aria-label="Music CD discs" style="background:radial-gradient(circle at 45% 50%,#c9a58e,#a9b0b4 70%,transparent 71%)"></div>
      <p class="product-name">Eiusmod tempor incididunt ut<br>labore et dolore magna al</p>
      <p class="price">$150</p>
      <div class="actions"><span class="btn btn-cart">Add to cart</span><span class="btn btn-view">View</span></div>
    </div>
    <div class="product" style="left:234px">
      <div class="product-image" role="img" aria-label="Floral summer dress" style="background:linear-gradient(#fff,#ddd5cc 30%,#cfc5ba 90%,#fff);width:80px;margin-left:22px"></div>
      <p class="product-name">Tempor incididunt ut labore et<br>dolore magna al Eiusmod</p>
      <p class="price">$200</p>
      <div class="actions"><span class="btn btn-cart">Add to cart</span><span class="btn btn-view">View</span></div>
    </div>
    <div class="product" style="left:434px">
      <div class="product-image" role="img" aria-label="Scarf necklace with beads" style="background:radial-gradient(circle,transparent 35%,#7a8a3a 36%,#a07a3a 60%,transparent 62%)"></div>
      <p class="product-name">Incididunt ut labore et dolore<br>magna al</p>
      <p class="price">$800</p>
      <div class="actions"><span class="btn btn-cart">Add to cart</span><span class="btn btn-view">View</span></div>
    </div>
    <div class="product" style="left:634px">
      <div class="product-image" role="img" aria-label="Green chiffon blouse" style="background:radial-gradient(circle,#1fbf5a 50%,transparent 62%)"></div>
      <p class="product-name">Ut labore et dolore magna al<br>Eiusmod incididunt &nbsp;tempor</p>
      <p class="price">$300</p>
      <div class="actions"><span class="btn btn-cart">Add to cart</span><span class="btn btn-view">View</span></div>
    </div>
    <div class="rule" style="top:547px"></div>
    <div class="feature" style="left:14px">
      <h3>PRODUCTS AND SELL ONLINE</h3>
      <p>Cras commodo risus eget est aliquet elementum. In volutpat magna sit amet ligula imperdiet</p>
      <span class="cta">CLICK HERE</span>
      <div class="feature-art" role="img" aria-label="Red folder with hard drive" style="background:linear-gradient(135deg,#e33,#9b1010)"></div>
    </div>
    <div class="feature red" style="left:278px">
      <h3>BOOK APPOINTMENT</h3>
      <p>Risus eget est aliquet elemen-tum. In volutpat magna sit amet ligula imperdiet</p>
      <span class="cta">CLICK HERE</span>
      <div class="feature-art" role="img" aria-label="Calendar icon" style="background:linear-gradient(#3a6fd0 20%,#f2f2f2 21%,#dcdcdc);top:40px;right:2px;height:86px"></div>
    </div>
    <div class="feature" style="left:541px">
      <h3>DONATE</h3>
      <p>Eget est aliquet elementum. In volutpat magna sit amet ligula imperdiet</p>
      <span class="cta">CLICK HERE</span>
      <div class="feature-art" role="img" aria-label="Donation can with coins" style="background:linear-gradient(#8a8a8a,#5a5a5a 60%,#8b1a22);border-radius:10px;width:72px;height:90px;top:24px"></div>
    </div>
  </main>
  <footer class="site-footer">
    <div>Home | About | Products | Feedback | Donate</div>
    <div>© 2012 PICH LEAKENA. All Rights Reserved</div>
    <div class="payments"><span>CoinLark</span><span>Pavora</span><span>Cardlyn</span><span>Quickbay</span><span>Norvis</span><span class="social">Friendloop</span><span class="social">Chirpnet</span></div>
  </footer>
</div>
</body>
</html>
```